Professional Services (B-2-B) Business Cards (Front & Back)

Corvantis is a business-to-business professional services company in the legal sector. They typically present to c-suite and executive functions who are looking for providers with expertise, and experience. Our business card should look and feel professional and contemporary, but we are not a startup tech company, so we want the tone to be more mature.

```html
<!DOCTYPE html>
<html lang="en">
<head>
<meta charset="utf-8">
<title>Corvantis Business Cards</title>
<link href="https://fonts.googleapis.com/css2?family=Montserrat:wght@400;500;700&display=swap" rel="stylesheet">
<style>
  :root {
    --backdrop: #b1b2ae;
    --card-white: #ffffff;
    --navy: #052f72;
    --navy-deep: #03306f;
    --navy-tint: #1a4fa8;
    --text-grey: #5d6168;
    --rule: #3b5a9a;
  }
  * { margin: 0; padding: 0; box-sizing: border-box; }
  html, body {
    width: 1200px; height: 801px; overflow: hidden;
    background: var(--backdrop);
    font-family: "Montserrat", Arial, sans-serif;
  }
  .stage {
    position: relative; width: 1200px; height: 801px;
    display: flex; align-items: center; justify-content: center; gap: 40px;
  }
  .card {
    position: relative; width: 540px; height: 309px;
    box-shadow: 0 6px 18px rgba(0,0,0,0.18);
  }
  .card--front { background: var(--card-white); }
  .card--back { background: var(--navy-deep); display: flex; align-items: center; justify-content: center; }

  .wordmark {
    display: flex; align-items: center; gap: 14px;
    font-weight: 500; letter-spacing: 0.42em; text-transform: uppercase;
  }
  .wordmark__square { width: 14px; height: 14px; flex: none; }
  .card--front .wordmark {
    position: absolute; left: 44px; top: 170px;
    font-size: 20px; color: var(--navy);
  }
  .card--front .wordmark__square { background: var(--navy); }
  .card--back .wordmark { font-size: 30px; color: var(--navy-tint); }
  .card--back .wordmark__square { background: var(--navy-tint); width: 20px; height: 20px; }

  .divider {
    position: absolute; left: 284px; top: 120px;
    width: 1px; height: 150px; background: var(--rule);
  }
  .contact { position: absolute; left: 306px; top: 62px; }
  .contact__name {
    font-weight: 700; font-size: 24px; color: var(--navy);
    letter-spacing: 0.02em; text-transform: uppercase; line-height: 1.1;
  }
  .contact__title { font-size: 13px; color: var(--text-grey); margin-top: 4px; margin-bottom: 14px; }
  .contact__list { list-style: none; }
  .contact__item {
    display: flex; align-items: center; gap: 8px;
    font-size: 12.5px; color: var(--text-grey); line-height: 1.6;
  }
  .contact__icon { width: 10px; height: 10px; flex: none; fill: none; stroke: var(--navy); stroke-width: 1.4; }
</style>
</head>
<body>
<main class="stage">
  <section class="card card--front" aria-label="Business card front">
    <div class="wordmark"><span class="wordmark__square"></span>Corvantis</div>
    <div class="divider"></div>
    <div class="contact">
      <h1 class="contact__name">Marcus Ellery</h1>
      <p class="contact__title">President &amp; CEO</p>
      <ul class="contact__list">
        <li class="contact__item">
          <svg class="contact__icon" viewBox="0 0 10 10"><path d="M2 1 L4 1 L4.5 3 L3.3 3.8 Q4.5 6 6.2 6.7 L7 5.5 L9 6 L9 8 Q5 9 2 5 Q1 3 2 1 Z"/></svg>
          (415) 555 - 0172
        </li>
        <li class="contact__item">
          <svg class="contact__icon" viewBox="0 0 10 10"><rect x="2.5" y="1" width="5" height="8" rx="1"/></svg>
          (203) 555 - 0148
        </li>
        <li class="contact__item">
          <svg class="contact__icon" viewBox="0 0 10 10"><rect x="1" y="2" width="8" height="6"/><path d="M1 2 L5 5.5 L9 2"/></svg>
          mellery@corvantis.law
        </li>
        <li class="contact__item">
          <svg class="contact__icon" viewBox="0 0 10 10"><circle cx="5" cy="5" r="4"/><path d="M1 5 H9 M5 1 Q2.5 5 5 9 M5 1 Q7.5 5 5 9"/></svg>
          www.corvantis.law
        </li>
      </ul>
    </div>
  </section>

  <section class="card card--back" aria-label="Business card back">
    <div class="wordmark"><span class="wordmark__square"></span>Corvantis</div>
  </section>
</main>
</body>
</html>
```